Auto glazing business card design

need a business card design for my company, the logo will be provided with an inspirational design as well.
It is for an auto glazing business in Australia.
I would like to have the basic details on the card as my name, phone number, email adress and website.
I suppose the challenge will be to fit a long email adress on a small business card.

Target Market(s)

autoglazing customers, retail mostly

Industry/Entity Type

auto glazing

Contact Information for Business Card

logo, name, phone, email and website

Colors
0054AA
0677BA
7BADD7
CADEEF
E8F1F8
0094D4
00A9DD
6FCCEA
C7EBF8
E9F6FB

Requirements
Must have
• logo, business details, maybe QR code

```html
<!DOCTYPE html>
<html lang="en">
<head>
<meta charset="utf-8">
<title>Clearline Mobile Glazing – Business Card</title>
<link href="https://fonts.googleapis.com/css2?family=Roboto:wght@400;500;700&display=swap" rel="stylesheet">
<style>
  :root {
    --page-bg: #c4c6c9;
    --card-white: #ffffff;
    --card-navy: #001b36;
    --ink-navy: #0d1b30;
    --ink-body: #1c2433;
    --teal: #1f8fb0;
    --teal-light: #3fb6c8;
    --brand-blue: #0677ba;
    --emboss-blue: #1d4a6e;
    --edge-cyan: #4cc3d4;
  }
  * { margin: 0; padding: 0; box-sizing: border-box; }
  html, body {
    width: 1200px;
    height: 800px;
    overflow: hidden;
    background: var(--page-bg);
    font-family: "Roboto", Arial, sans-serif;
  }
  .stage {
    width: 1200px;
    height: 800px;
    display: flex;
    align-items: center;
    justify-content: center;
    gap: 40px;
  }
  .card {
    width: 520px;
    height: 318px;
    border-radius: 18px;
    position: relative;
    overflow: hidden;
    box-shadow: 0 14px 30px rgba(0, 0, 0, 0.22);
    border-bottom: 3px solid var(--edge-cyan);
  }

  /* Front */
  .card-front { background: var(--card-white); }
  .front-brand {
    position: absolute;
    left: 44px;
    bottom: 52px;
    display: flex;
    align-items: center;
    gap: 12px;
  }
  .front-brand .brand-square {
    width: 22px;
    height: 22px;
    background: var(--brand-blue);
  }
  .front-brand .brand-name {
    font-size: 22px;
    font-weight: 700;
    letter-spacing: 2px;
    color: var(--brand-blue);
    text-transform: uppercase;
  }
  .contact-block {
    position: absolute;
    left: 250px;
    top: 70px;
    color: var(--ink-body);
  }
  .person-name {
    font-size: 24px;
    font-weight: 700;
    letter-spacing: 0.5px;
    color: var(--ink-navy);
    text-transform: uppercase;
  }
  .person-role {
    font-size: 15px;
    margin-top: 4px;
  }
  .role-rule {
    width: 62px;
    height: 2px;
    background: var(--teal);
    margin: 6px 0 12px;
  }
  .contact-line {
    font-size: 13.5px;
    line-height: 21px;
    letter-spacing: 0.3px;
    white-space: nowrap;
  }
  .contact-line.phone { letter-spacing: 1.5px; font-size: 15px; }

  /* Back */
  .card-back {
    background: var(--card-navy);
    display: flex;
    flex-direction: column;
    align-items: center;
    justify-content: center;
  }
  .back-brand {
    color: var(--emboss-blue);
    font-weight: 700;
    text-transform: uppercase;
    text-align: center;
    font-size: 30px;
    letter-spacing: 6px;
    line-height: 42px;
  }
</style>
</head>
<body>
  <main class="stage">
    <section class="card card-front" aria-label="Business card front">
      <div class="front-brand">
        <span class="brand-square"></span>
        <span class="brand-name">Clearline</span>
      </div>
      <div class="contact-block">
        <h1 class="person-name">Sam Whitford</h1>
        <p class="person-role">Director</p>
        <div class="role-rule"></div>
        <p class="contact-line phone">0412 555 018</p>
        <p class="contact-line">info@clearlinemobileglazing.com.au</p>
        <p class="contact-line">www.clearlinemobileglazing.com.au</p>
      </div>
    </section>

    <section class="card card-back" aria-label="Business card back">
      <p class="back-brand">Clearline<br>Mobile Glazing</p>
    </section>
  </main>
</body>
</html>
```